Design Packaging for Brisa Alta Coffee

Please look at website at www.brisaltacoffeeworks.example
Need packaging for new coffee company. The size is: 6 x 9 x 3"

```html
<!DOCTYPE html>
<html lang="en">
<head>
<meta charset="utf-8">
<title>Brisa Alta Coffee – Costa Rica Coffee Bag</title>
<link href="https://fonts.googleapis.com/css2?family=Oswald:wght@400;500;600&display=swap" rel="stylesheet">
<style>
  :root {
    --backdrop: #dff4fb;
    --magenta-deep: #96003a;
    --magenta-light: #b8185c;
    --sky-band: #86abc6;
    --sky-side: #8db4cd;
    --sky-side-dark: #6f97b3;
    --sun-yellow: #f2c10f;
    --brand-brown: #3d2a1a;
    --maroon-text: #6e0a2a;
    --red-text: #c8102e;
    --badge-blue: #86abc6;
    --badge-ink: #3e2a4a;
    --art-dark: #1c1412;
    --art-gold: #dcae12;
    --art-red: #d52a1e;
  }
  * { margin: 0; padding: 0; box-sizing: border-box; }
  html, body { width: 1200px; height: 900px; overflow: hidden; }
  body {
    background: var(--backdrop);
    font-family: "Oswald", "Arial Narrow", sans-serif;
    position: relative;
  }
  .bag-dieline {
    position: absolute;
    left: 285px; top: 135px;
    width: 630px; height: 630px;
    display: flex;
  }
  .front-panel {
    position: relative;
    width: 420px; height: 630px;
    background: linear-gradient(135deg, var(--magenta-deep) 0%, var(--magenta-deep) 45%, var(--magenta-light) 100%);
    overflow: hidden;
  }
  .brand-band {
    position: absolute; left: 0; top: 0;
    width: 100%; height: 64px;
    background: var(--sky-band);
    display: flex; align-items: center; justify-content: center; gap: 10px;
  }
  .brand-dot {
    width: 16px; height: 16px; border-radius: 50%;
    background: var(--brand-brown);
  }
  .brand-name {
    font-weight: 600; font-size: 22px; letter-spacing: 1px;
    color: var(--brand-brown); text-transform: uppercase;
  }
  .product-title {
    position: absolute; left: 0; top: 90px; width: 100%;
    text-align: center; color: var(--sun-yellow);
    font-weight: 500; text-transform: uppercase; line-height: 0.95;
  }
  .product-title .origin { display: block; font-size: 72px; }
  .product-title .kind { display: block; font-size: 118px; letter-spacing: 2px; }
  .toucan-art {
    position: absolute; left: 0; top: 320px;
    width: 250px; height: 310px;
  }
  .blend-info {
    position: absolute; left: 268px; top: 420px;
    width: 130px; text-align: center; color: var(--sun-yellow);
  }
  .blend-info .percent { display: block; font-size: 40px; font-weight: 500; line-height: 1; }
  .blend-info .variety { display: block; font-size: 38px; font-weight: 400; line-height: 1.1; }
  .premium-badge {
    display: inline-block; margin-top: 6px;
    background: var(--badge-blue); color: var(--badge-ink);
    font-size: 14px; letter-spacing: 4px; padding: 2px 8px 2px 12px; border-radius: 2px;
  }
  .base-wave { position: absolute; left: 0; bottom: 0; width: 420px; height: 80px; }
  .net-weight {
    position: absolute; right: 36px; bottom: 18px;
    font-size: 28px; color: var(--maroon-text); font-weight: 500;
  }
  .side-panel {
    position: relative;
    width: 210px; height: 630px;
    background: linear-gradient(90deg, var(--sky-side) 0%, var(--sky-side) 70%, var(--sky-side-dark) 100%);
    padding: 170px 26px 0 26px;
  }
  .side-brand {
    display: flex; align-items: center; gap: 6px;
  }
  .side-brand .brand-dot { width: 10px; height: 10px; }
  .side-brand .brand-name { font-size: 13px; letter-spacing: 0.5px; }
  .side-title {
    margin-top: 12px; font-size: 17px; font-weight: 500;
    color: var(--red-text); text-transform: uppercase;
  }
  .side-copy {
    margin-top: 6px; font-size: 8.5px; line-height: 1.75;
    text-transform: uppercase; color: var(--red-text);
    text-align: justify; letter-spacing: 0.3px;
  }
</style>
</head>
<body>
  <main class="bag-dieline">
    <section class="front-panel">
      <header class="brand-band">
        <span class="brand-dot"></span>
        <span class="brand-name">Brisa Alta Coffee</span>
      </header>

      <h1 class="product-title">
        <span class="origin">Costa Rica</span>
        <span class="kind">Coffee</span>
      </h1>

      <svg class="toucan-art" role="img" aria-label="Illustration of a toucan with a large yellow and red beak among red tropical leaves and hills" viewBox="0 0 250 310" preserveAspectRatio="none">
        <defs>
          <linearGradient id="artTones" x1="0" y1="1" x2="1" y2="0">
            <stop offset="0" stop-color="var(--art-dark)"/>
            <stop offset="0.5" stop-color="var(--art-red)"/>
            <stop offset="1" stop-color="var(--art-gold)"/>
          </linearGradient>
        </defs>
        <rect width="250" height="310" fill="url(#artTones)" opacity="0.85"/>
      </svg>

      <div class="blend-info">
        <span class="percent">100%</span>
        <span class="variety">arabica</span>
        <span class="premium-badge">PREMIUM</span>
      </div>

      <svg class="base-wave" viewBox="0 0 420 80" preserveAspectRatio="none" aria-hidden="true">
        <path d="M0 80 L0 70 Q120 20 230 32 Q330 42 420 8 L420 80 Z" fill="var(--sky-band)"/>
        <path d="M330 80 L420 52 L420 80 Z" fill="var(--sun-yellow)"/>
      </svg>
      <span class="net-weight">700gr</span>
    </section>

    <aside class="side-panel">
      <div class="side-brand">
        <span class="brand-dot"></span>
        <span class="brand-name">Brisa Alta Coffee</span>
      </div>
      <h2 class="side-title">Costa Rica Coffee</h2>
      <p class="side-copy">Grown on volcanic slopes above the central valley, these beans ripen slowly in cool mountain air. Each cherry is picked by hand at peak sweetness, washed in spring water and dried in the sun on raised beds. The result is a bright, clean cup with notes of honey, citrus and dark cocoa. Brew with fresh water just off the boil, use two spoons per cup and enjoy within four weeks of opening. Store sealed in a cool, dry place away from light. Roasted and packed with care for a gentle morning ritual.</p>
    </aside>
  </main>
</body>
</html>
```